New Fun, Positive, energised looking Business Card Needed for High Achiever Coach

I am looking for a two sided full colour business card. I am self employed and have recently re branded my 1-2-1 work re-vitalising high achievers. My target client base for these cards is therefore high achievers - usually aged 40 -55, they are often entrepreneurs, CEO or work in banking and finance and 2/3 are male. I work with them on 90 day or 6 month coaching programs to help them live their success in a healthier, more sustainable and fulfiiled way. They pay for this privately so though they are corporate types the cards need not look 'corporate'. I want to portray the idea of transformation, vitality and re-connecting.
You can get a feel for the look I like on my new website: corinvale.co.uk
I want to use this logo with strapline (Re-Vitalising High Achievers) (I purchased off Logoharbor) and font/ colours (the turquoise and green).
Details to include on the card:
www.corinvale.co.uk
+44 7915 264318
mira@corinvale.co.uk
skype: miracorin
I'd also like to include:
Do you struggle to switch off? Want to be healthier and feel fitter? Want closer relationships? More clarity over the direction you are headed? I can help you do these things using integrated mind-body techniques. Visit corinvale.co.uk TODAY to apply for a FREE Breakthrough session.
BUT if that is too much text for a card I am open to advice/ammendments.
Updates
Thanks for your design - I am considering them. PLease change the wording to :

```html
<!DOCTYPE html>
<html lang="en">
<head>
<meta charset="utf-8">
<title>Mira Corin – Business Card</title>
<link rel="stylesheet" href="https://fonts.googleapis.com/css2?family=Alfa+Slab+One&family=Allura&family=Open+Sans:wght@400;700&display=swap">
<style>
  :root {
    --backdrop: #6d6e71;
    --card-white: #ffffff;
    --turquoise: #0aa4cc;
    --brand-green: #5cbd6b;
    --contact-grey: #a7a9ac;
    --icon-grey: #9d9fa2;
    --back-text: #ffffff;
  }
  * { box-sizing: border-box; margin: 0; padding: 0; }
  html, body {
    width: 1200px;
    height: 1001px;
    overflow: hidden;
    background: var(--backdrop);
  }
  .canvas {
    position: relative;
    width: 1200px;
    height: 1001px;
    background: var(--backdrop);
  }
  .card {
    position: absolute;
    top: 36px;
    width: 534px;
    height: 936px;
    overflow: hidden;
  }
  .card--front {
    left: 52px;
    background: var(--card-white);
  }
  .card--back {
    left: 637px;
    top: 32px;
    height: 935px;
    background: var(--brand-green);
  }
  .front-swoosh {
    position: absolute;
    inset: 0;
    width: 534px;
    height: 936px;
  }
  .front-swoosh path { fill: var(--turquoise); }

  .brand-mark {
    position: absolute;
    left: 148px;
    top: 84px;
    width: 136px;
    height: 136px;
    border-radius: 50%;
    background: var(--brand-green);
  }
  .brand-name {
    position: absolute;
    left: 22px;
    top: 306px;
    font-family: "Alfa Slab One", serif;
    font-weight: 400;
    font-size: 50px;
    line-height: 1;
    color: var(--turquoise);
    letter-spacing: 0.5px;
  }
  .brand-strapline {
    position: absolute;
    left: 24px;
    top: 368px;
    font-family: "Allura", cursive;
    font-size: 36px;
    line-height: 1;
    color: var(--turquoise);
  }

  .contact-list {
    position: absolute;
    left: 126px;
    top: 558px;
    list-style: none;
  }
  .contact-item {
    display: flex;
    align-items: center;
    height: 34px;
    font-family: "Open Sans", sans-serif;
    font-size: 26px;
    color: var(--contact-grey);
    line-height: 1;
  }
  .contact-icon {
    width: 30px;
    height: 24px;
    margin-right: 10px;
    flex: none;
  }
  .contact-icon path,
  .contact-icon circle,
  .contact-icon rect { fill: var(--icon-grey); }

  .pitch {
    position: absolute;
    left: 26px;
    right: 26px;
    top: 672px;
    font-family: "Open Sans", sans-serif;
    font-size: 21.5px;
    line-height: 28.5px;
    color: var(--back-text);
    text-align: center;
  }
  .pitch strong { font-weight: 700; }
</style>
</head>
<body>
<main class="canvas">

  <section class="card card--front" aria-label="Card front">
    <svg class="front-swoosh" viewBox="0 0 534 936" aria-hidden="true">
      <path d="M224 0 C 380 38 500 120 534 218 L534 0 Z"/>
      <path d="M0 728 C 170 790 380 872 512 936 L0 936 Z"/>
    </svg>

    <div class="brand-mark" aria-hidden="true"></div>
    <h1 class="brand-name">Mira Corin</h1>
    <p class="brand-strapline">Re-Vitalising High Achievers</p>

    <ul class="contact-list">
      <li class="contact-item">
        <svg class="contact-icon" viewBox="0 0 30 24" aria-hidden="true">
          <path d="M2 7 C 8 1 22 1 28 7 L25 11 L20 9 L19 6 C 16 5 14 5 11 6 L10 9 L5 11 Z"/>
          <path d="M9 11 L21 11 L25 19 L5 19 Z"/>
        </svg>
        <span>+44 7915 264318</span>
      </li>
      <li class="contact-item">
        <svg class="contact-icon" viewBox="0 0 30 24" aria-hidden="true">
          <circle cx="13" cy="12" r="10"/>
        </svg>
        <span>miracorin</span>
      </li>
      <li class="contact-item">
        <svg class="contact-icon" viewBox="0 0 30 24" aria-hidden="true">
          <circle cx="13" cy="12" r="10"/>
          <path d="M3 11 H23 V13 H3 Z M12 2 H14 V22 H12 Z" style="fill:#ffffff"/>
        </svg>
        <span>www.corinvale.co.uk</span>
      </li>
      <li class="contact-item">
        <svg class="contact-icon" viewBox="0 0 30 24" aria-hidden="true">
          <rect x="2" y="5" width="22" height="15"/>
          <path d="M2 5 L13 14 L24 5" style="fill:none;stroke:#ffffff;stroke-width:2"/>
        </svg>
        <span>mira@corinvale.co.uk</span>
      </li>
    </ul>
  </section>

  <section class="card card--back" aria-label="Card back">
    <p class="pitch">
      Do you struggle to switch off? Want to be healthier and feel fitter? Want closer relationships? More clarity over the direction you are headed? I can help you do these things using integrated mind-body techniques.<br>
      Visit <strong>corinvale.co.uk</strong><br>
      TODAY to apply for a FREE Breakthrough session.
    </p>
  </section>

</main>
</body>
</html>
```